Harbor Crest Seminar Postcard Design

I need a postcard designed that is 5.5" x 8.5". Color front and back with space for an address block and postal indicia. I will provide the bullet points and copy. I need assistance with the layout, organization and perhaps a couple of images, etc. This postcard will drive individuals to a web site to register for a 90-minute seminar teaching them how to minimize or eliminate their income taxes during retirement.
Target Market(s)
Married Couples, ages 50 - 70. Successful and affluent. People that appreciate and value professional advice and relationships.
Requirements
Must have
- Bright and Bold.  Compelling and attention grabbing.
Call to action #1 - Go to website immediately for further information.
Call to action #2 - Call the office immediately to register.

```html
<!DOCTYPE html>
<html lang="en">
<head>
<meta charset="utf-8">
<title>Harbor Crest Seminar Postcard</title>
<link rel="stylesheet" href="https://fonts.googleapis.com/css2?family=Cinzel:wght@500;600&family=Didact+Gothic&family=Fira+Sans:ital,wght@0,600;1,500;1,600&display=swap">
<style>
  :root {
    --page-bg: #e9e6e1;
    --card-bg: #ffffff;
    --brand-blue: #1d68a8;
    --body-grey: #5a5a5a;
    --cta-grey: #555555;
    --photo-top: #d9cbb4;
    --photo-mid: #3a3530;
    --photo-low: #6d5a4c;
  }
  * { margin: 0; padding: 0; box-sizing: border-box; }
  html, body {
    width: 1200px; height: 818px; overflow: hidden;
    background: var(--page-bg);
  }
  .postcard {
    position: absolute; left: 50px; top: 54px;
    width: 1100px; height: 710px;
    background: var(--card-bg);
    box-shadow: 0 4px 14px rgba(0,0,0,0.25);
    overflow: hidden;
  }
  .headline {
    position: absolute; left: 50px; top: 36px; width: 520px;
    font-family: "Cinzel", serif; font-weight: 600;
    font-size: 37px; line-height: 52px; letter-spacing: 0.5px;
    color: var(--brand-blue); text-align: center;
  }
  .intro {
    position: absolute; left: 62px; top: 212px; width: 460px;
    font-family: "Didact Gothic", sans-serif;
    font-size: 24.5px; line-height: 30.5px;
    color: var(--body-grey);
  }
  .intro-line { display: block; text-align: justify; text-align-last: justify; white-space: nowrap; }
  .intro-line:last-child { text-align-last: left; }
  .register-button {
    position: absolute; left: 107px; top: 412px;
    width: 367px; height: 127px;
    background: var(--brand-blue);
    border: 4px solid #fff; border-radius: 14px;
    box-shadow: 0 0 0 1px #c9c9c9, 0 3px 6px rgba(0,0,0,0.3);
    display: flex; align-items: center; justify-content: center;
    font-family: "Fira Sans", sans-serif; font-style: italic; font-weight: 600;
    font-size: 29px; line-height: 38px; color: #fff; text-align: center;
  }
  .call-prompt {
    position: absolute; left: 40px; top: 566px; width: 506px;
    font-family: "Fira Sans", sans-serif; font-style: italic; font-weight: 500;
    font-size: 26px; color: var(--cta-grey); text-align: center;
  }
  .phone-line {
    position: absolute; left: 40px; top: 628px; width: 506px;
    display: flex; align-items: center; justify-content: center; gap: 10px;
    font-family: "Fira Sans", sans-serif; font-weight: 600;
    font-size: 37px; color: var(--brand-blue);
  }
  .phone-icon { width: 40px; height: 40px; flex: none; }
  .venue-art {
    position: absolute; left: 560px; top: 0; width: 540px; height: 710px;
  }
</style>
</head>
<body>
  <main class="postcard">
    <h1 class="headline">How to Minimize or Eliminate Income Taxes During Retirement?</h1>
    <p class="intro">
      <span class="intro-line">A Unique, One-Of-A-Kind Program</span>
      <span class="intro-line">Reveals Little Known Secrets Used By</span>
      <span class="intro-line">America’s Wealthiest Families To</span>
      <span class="intro-line">Reduce And Even Eliminate Their</span>
      <span class="intro-line">Income Taxes During Their Retirement</span>
      <span class="intro-line">Years</span>
    </p>
    <div class="register-button">Register for a 90-minute<br>seminar teaching</div>
    <p class="call-prompt">Call the office immediately to register</p>
    <p class="phone-line">
      <svg class="phone-icon" viewBox="0 0 40 40" aria-hidden="true">
        <circle cx="20" cy="20" r="17" fill="none" stroke="var(--brand-blue)" stroke-width="3"/>
        <path d="M14 10c-2 1-4 3-3 7 1 5 6 11 11 13 3 1 5 0 7-2l-3-4c-1 0-2 1-3 1-3-1-6-5-7-8 0-1 1-2 2-2z" fill="var(--brand-blue)"/>
      </svg>
      (555) 214 8630
    </p>
    <svg class="venue-art" viewBox="0 0 540 710">
      <defs>
        <linearGradient id="hallTones" x1="0" y1="0" x2="0" y2="1">
          <stop offset="0" stop-color="var(--photo-top)"/>
          <stop offset="0.3" stop-color="#a89a86"/>
          <stop offset="0.45" stop-color="var(--photo-mid)"/>
          <stop offset="0.6" stop-color="#8a7565"/>
          <stop offset="1" stop-color="var(--photo-low)"/>
        </linearGradient>
      </defs>
      <path role="img" aria-label="Photo of a seminar audience in a lecture hall facing a speaker and projection screen"
            d="M43,0 C95,180 110,420 36,710 L469,710 C495,500 490,200 423,0 Z" fill="url(#hallTones)"/>
      <path d="M28,0 C80,180 95,420 20,710" fill="none" stroke="var(--brand-blue)" stroke-width="3"/>
      <path d="M436,0 C505,200 510,500 484,710" fill="none" stroke="var(--brand-blue)" stroke-width="2"/>
    </svg>
  </main>
</body>
</html>
```